Teilnehmerzertifikat für Expeditionsmobil
Zielgruppe
Wir bitten alles Rund um das Thema Expeditionsmobil an. Unter anderem unsere Lagerfeuer und Weite Fahrt nach Tunesien und dafür benötige ich ein Teilnehmer Zertifikat.
Aufgabenstellung
Im Hintergrund soll ein Bild von der Sahara verarbeitet sein und im Vordergrund möchte ich von jedem Teilnehmer ein Bild mit dem eigenen Expeditonsfahrzeug einfügen. Das Zertifikat soll persöhnlich und wie von einem Freund sein

```html
<!DOCTYPE html>
<html lang="de">
<head>
<meta charset="utf-8">
<title>Teilnehmerzertifikat – Lagerfeuer und Weite Fahrt Tunesien</title>
<link rel="stylesheet" href="https://fonts.googleapis.com/css2?family=Anton&family=Black+Ops+One&family=Fira+Sans+Condensed:wght@500;800&family=Rubik+Dirt&display=swap">
<style>
  :root {
    --paper: #ffffff;
    --sky-top: #7fa7c4;
    --sky-mid: #e9c39a;
    --sunset: #f07a22;
    --sunset-deep: #d9471c;
    --horizon: #8a4a2c;
    --sand: #8f5a40;
    --sand-dark: #6b3f2d;
    --ink: #2a2320;
    --white: #ffffff;
    --tag-ink: #6b6b6b;
    --polaroid-shadow: rgba(0,0,0,0.35);
    --photo-top: #3d6ea3;
    --photo-mid: #e0803a;
    --photo-low: #2c2a2a;
  }
  * { margin: 0; padding: 0; box-sizing: border-box; }
  html, body { width: 848px; height: 1200px; overflow: hidden; background: var(--paper); }
  .certificate { position: relative; width: 848px; height: 1200px; background: var(--paper); overflow: hidden; }

  .desert-backdrop {
    position: absolute; left: 22px; top: 14px; width: 804px; height: 1146px;
    background: linear-gradient(180deg,
      var(--sky-top) 0%, #b9c3c8 12%, var(--sky-mid) 24%, #f3a55e 34%,
      var(--sunset) 41%, var(--sunset-deep) 47%, var(--horizon) 50%,
      var(--sand) 58%, #9b6448 72%, var(--sand-dark) 100%);
  }

  .tour-title {
    position: absolute; left: 340px; top: 78px; width: 240px;
    font-family: "Anton", "Impact", sans-serif; font-weight: 400; color: var(--white);
    text-transform: uppercase; line-height: 1; text-align: right; white-space: nowrap;
  }
  .tour-title .line-big { display: block; font-size: 38px; letter-spacing: 0.5px; margin-bottom: 6px; }
  .tour-title .line-small { font-size: 20px; }
  .tour-title .country-tag {
    display: block; margin-top: 10px; padding: 6px 0 4px;
    background: var(--white); color: var(--tag-ink); font-size: 34px; letter-spacing: 3px; text-align: center;
  }

  .certificate-word {
    position: absolute; left: 24px; top: 340px; width: 804px;
    font-family: "Rubik Dirt", "Impact", sans-serif; font-size: 106px;
    color: var(--white); opacity: 0.55; letter-spacing: 4px; text-align: center;
    line-height: 1; white-space: nowrap; transform: scaleY(1.55); transform-origin: center top;
  }

  .participant-name {
    position: absolute; left: 0; top: 496px; width: 848px; text-align: center;
    font-family: "Black Ops One", "Impact", sans-serif; font-weight: 400; font-size: 32px;
    color: var(--ink); letter-spacing: 1px; white-space: nowrap;
  }

  .polaroid {
    position: absolute; left: 52px; top: 578px; width: 364px; height: 418px;
    background: var(--white); transform: rotate(-1.5deg);
    box-shadow: 4px 6px 14px var(--polaroid-shadow);
  }
  .polaroid-photo {
    position: absolute; left: 18px; top: 34px; width: 326px; height: 330px;
    background: linear-gradient(180deg, var(--photo-top) 0%, #8aa0b8 28%, var(--photo-mid) 50%, #6a3d2a 72%, var(--photo-low) 100%);
  }
  .polaroid-caption {
    position: absolute; left: 0; top: 226px; width: 100%; text-align: center;
    font-family: "Rubik Dirt", "Impact", sans-serif; font-size: 30px; line-height: 1.1;
    color: var(--white); white-space: nowrap;
  }
  .pin-flag { position: absolute; left: 232px; top: 548px; }

  .greeting {
    position: absolute; left: 478px; top: 612px; width: 320px;
    font-family: "Fira Sans Condensed", "Arial Narrow", sans-serif; font-weight: 500;
    font-size: 16.5px; line-height: 34px; color: var(--white); white-space: nowrap;
  }
  .signature-line {
    position: absolute; left: 480px; top: 975px; width: 292px; height: 1.5px;
    background: var(--white);
  }

  .partner {
    position: absolute; top: 1040px;
    display: flex; align-items: center; gap: 10px; white-space: nowrap;
    font-family: "Fira Sans Condensed", "Arial Narrow", sans-serif; font-weight: 800;
    font-size: 28px; line-height: 1; color: var(--white); text-transform: uppercase; letter-spacing: 0.5px;
  }
  .partner-travel { left: 97px; }
  .partner-tech { left: 420px; }
  .partner-dot { width: 28px; height: 28px; border-radius: 50%; background: var(--white); flex: none; }
</style>
</head>
<body>
<main class="certificate">
  <div class="desert-backdrop" role="img" aria-label="Foto der Sahara bei Sonnenuntergang: blauer Himmel, orange glühender Horizont und Sanddünen mit Reifenspuren"></div>

  <h1 class="tour-title">
    <span class="line-big">Lagerfeuer <span class="line-small">und</span></span>
    <span class="line-big">Weite Fahrt</span>
    <span class="country-tag">Tunesien</span>
  </h1>

  <div class="certificate-word">ZERTIFIKAT</div>

  <h2 class="participant-name">VORNAME NACHNAME</h2>

  <figure class="polaroid">
    <div class="polaroid-photo" role="img" aria-label="Platz für das Foto des Teilnehmers mit dem eigenen Expeditionsmobil in der Wüste">
      <figcaption class="polaroid-caption">DUMMY<br>FÜR BILD</figcaption>
    </div>
  </figure>

  <svg class="pin-flag" width="34" height="40" viewBox="0 0 34 40" aria-hidden="true">
    <line x1="6" y1="4" x2="6" y2="38" stroke="#ffffff" stroke-width="2.5"/>
    <path d="M7 4 L30 8 L24 14 L30 20 L7 18 Z" fill="#ffffff" stroke="#cfcfcf" stroke-width="1"/>
  </svg>

  <p class="greeting">
    Ihr habt mit Begeisterung und<br>
    Abenteuerlust an unserer gemeinsamen<br>
    Reise durch Tunesien teilgenommen.<br>
    Mit eurem Expeditionsmobil habt ihr die<br>
    Wüste bezwungen, neue Freundschaften<br>
    geschlossen und die Magie dieses<br>
    einzigartigen Landes erlebt.<br>
    Danke, dass ihr Teil dieser besonderen<br>
    Tour wart – auf viele weitere Abenteuer!
  </p>
  <div class="signature-line"></div>

  <div class="partner partner-travel"><span class="partner-dot"></span>Kranichpfad Reisen</div>
  <div class="partner partner-tech"><span class="partner-dot"></span>Kranichpfad Technik</div>
</main>
</body>
</html>
```